| 希望する色 | ピンク系 追記事項: 淡いピンクでお願いします |
【 概要 】 当方はライブ配信者(ライバー)をマネジメントする事務所業を行っています。 弊社HP (https://kazenoha-office.co.jp/) 今回、ライブ配信者新規獲得のための広告バナーデザイン制作をお願いします。 【 依頼内容 】 ・サイズ:600×500、336×280、300×250、300×300 ・作成数:4種類(サイズのみ変えて4パターン) ・利用用途:リスティング広告、ウェブサイトなど 【 デザインイメージ 】 ・ターゲット層:25〜40歳女性、1日2時間程度ライブ配信を行う可処分時間がある(暇である)、今以上の収入が欲しい ・雰囲気:ペルソナに合わせて、オシャレさよりは視認性、わかりやすさを重視 【 訴求要素 】 ・在宅で手軽にできること ・月20万円程度稼げること ・事務所の規模:1600人が登録し、業界最大規模 【 提供素材 】 ・ラフ案:あり ・画像:なし ・文章:あり 【 報酬 】 1万円 その他ご質問等ありましたら、気軽にお問い合わせください。 ご応募をお待ちしております! |
| https://kazenoha-office.co.jp/ | ||
採用の理由
この作品がもっともイメージにあっておりましたので、採用させて頂きます。
応募者全員へのお礼・コメント
ご提案頂き、ありがとうございました。
魅力的なデザインが複数ありましたので、場合によっては追加発注させて頂きます。

```html
<!DOCTYPE html>
<html lang="ja">
<head>
<meta charset="utf-8">
<title>ライバー募集バナー</title>
<link rel="stylesheet" href="https://fonts.googleapis.com/css2?family=M+PLUS+Rounded+1c:wght@800;900&display=swap">
<style>
  :root {
    --pink: #f3709a;
    --pink-deep: #e94577;
    --pink-pale: #fde4ec;
    --white: #ffffff;
    --yellow: #fff37a;
    --button: #fff6a8;
    --blue: #1d6fd8;
  }
  * { margin: 0; padding: 0; box-sizing: border-box; }
  html, body { width: 1200px; height: 1000px; overflow: hidden; }
  body { font-family: "M PLUS Rounded 1c", sans-serif; font-weight: 900; }
  .banner {
    position: relative; width: 1200px; height: 1000px; overflow: hidden;
    background: linear-gradient(180deg, var(--white) 40%, var(--pink-pale) 100%);
  }
  .banner__backdrop { position: absolute; inset: 0; }
  .banner__portrait {
    position: absolute; left: 0; top: 190px; width: 560px; height: 700px;
    background: radial-gradient(ellipse at 45% 40%, #f4dcd2 0%, #d9b2a4 45%, #f7e6ea 100%);
  }
  .headline {
    position: absolute; left: 24px; top: 58px; color: var(--white);
    font-size: 112px; line-height: 1; letter-spacing: -2px;
    display: flex; align-items: center; gap: 10px;
  }
  .headline__play { width: 78px; height: 78px; flex: none; }
  .headline__small { font-size: 84px; }
  .income {
    position: absolute; left: 410px; top: 175px; color: var(--pink-deep);
    font-size: 118px; line-height: 1; letter-spacing: -2px;
  }
  .income__amount {
    color: var(--yellow); font-size: 150px;
    -webkit-text-stroke: 10px var(--pink-deep); paint-order: stroke fill;
  }
  .income__unit {
    color: var(--yellow); font-size: 118px;
    -webkit-text-stroke: 10px var(--pink-deep); paint-order: stroke fill;
  }
  .support {
    position: absolute; left: 555px; top: 395px; width: 600px;
    text-align: center; color: var(--pink-deep);
    font-size: 82px; line-height: 1.22;
  }
  .support__small { font-size: 58px; }
  .tagline {
    position: absolute; left: 510px; top: 760px; color: var(--blue);
    font-size: 58px; line-height: 1;
  }
  .tagline__small { font-size: 46px; }
  .footer {
    position: absolute; left: 0; bottom: 0; width: 1200px; height: 105px;
    background: var(--pink);
  }
  .footer__brand {
    position: absolute; left: 0; right: 0; top: 22px; text-align: center;
    color: var(--white); font-size: 54px; letter-spacing: 14px; line-height: 1;
  }
  .footer__cta {
    position: absolute; right: 90px; top: 20px; width: 200px; height: 66px;
    background: var(--button); border: 5px solid var(--pink-deep); border-radius: 10px;
    color: var(--pink-deep); font-size: 40px; line-height: 56px; text-align: center;
  }
</style>
</head>
<body>
  <div class="banner">
    <svg class="banner__backdrop" width="1200" height="1000" viewBox="0 0 1200 1000">
      <polygon points="0,0 1200,0 1200,120 0,440" fill="var(--pink)"/>
    </svg>

    <div class="banner__portrait" role="img" aria-label="スマートフォンを手に笑顔でライブ配信をする女性の写真"></div>

    <h1 class="headline">
      <svg class="headline__play" viewBox="0 0 80 80">
        <circle cx="40" cy="40" r="34" fill="none" stroke="var(--white)" stroke-width="9"/>
        <polygon points="32,24 56,40 32,56" fill="var(--white)"/>
      </svg>
      <span>LIVE配信<span class="headline__small">で</span></span>
    </h1>

    <p class="income">月収<span class="income__amount">20</span><span class="income__unit">万円!?</span></p>

    <p class="support">1600人登録<span class="support__small">の</span><br>専門事務所<span class="support__small">が</span><br>サポート</p>

    <p class="tagline">自宅<span class="tagline__small">で</span>お手軽ライブ配信♪</p>

    <footer class="footer">
      <span class="footer__brand">KAZENOHA</span>
      <span class="footer__cta">Click!</span>
    </footer>
  </div>
</body>
</html>
```